Graphic Design Project

We need a single page design that will be used as a regular white paper, providing communication advice & techniques.

We have an example that needs upgrading to look more professional and exciting.

Logo and icons will be provided.

Image provided for this example but will need to be able to add and remove new images relative to each new white paper.

Design will need to be on a format that is easily editable and can be converted into a PDF document. e.g MS Word.

Target Market(s)

Existing and potential corporate individuals and organisations

Industry/Entity Type

Communication

Requirements
Must have
• Logo, Icons & web address

```html
<!DOCTYPE html>
<html lang="en">
<head>
<meta charset="utf-8">
<title>Brightwell Communications — White Paper</title>
<link href="https://fonts.googleapis.com/css2?family=Didact+Gothic&family=Questrial&family=Poppins:wght@600&display=swap" rel="stylesheet">
<style>
  :root {
    --backdrop: #999999;
    --page: #ffffff;
    --ink: #231f20;
    --body-ink: #2b2b2b;
    --band-grey: #b7b6b6;
    --footer-grey: #bcbbbb;
    --orange: #f5a02a;
    --orange-deep: #f08c1c;
    --yellow: #fcc31b;
    --white: #ffffff;
  }
  * { margin: 0; padding: 0; box-sizing: border-box; }
  html, body { width: 1200px; height: 1000px; overflow: hidden; background: var(--backdrop); }
  .canvas { position: relative; width: 1200px; height: 1000px; background: var(--backdrop); }

  .page { position: absolute; left: 213px; top: 0; width: 587px; height: 1000px; background: var(--page); }

  .brand { position: absolute; left: 5px; top: 22px; display: flex; align-items: center; gap: 14px; }
  .brand-name { font-family: "Poppins", sans-serif; font-weight: 600; font-size: 36px; color: var(--ink); letter-spacing: -0.5px; }
  .brand-dot { width: 34px; height: 34px; border-radius: 50%; background: var(--orange); }

  .title-band { position: absolute; left: 0; top: 118px; width: 480px; height: 39px; background: var(--band-grey); }
  .title-band h1 { font-family: "Questrial", sans-serif; font-weight: 400; font-size: 22px; color: var(--ink); line-height: 39px; padding-left: 44px; }

  .column { position: absolute; top: 176px; width: 216px; font-family: "Didact Gothic", sans-serif; font-size: 9.6px; line-height: 22.8px; color: var(--body-ink); text-align: justify; }
  .column-left { left: 49px; }
  .column-right { left: 318px; }

  .summary { position: absolute; left: 0; top: 832px; width: 587px; height: 168px; background: var(--footer-grey); padding: 24px 18px 0 19px; }
  .summary p { font-family: "Didact Gothic", sans-serif; font-size: 9.6px; line-height: 23px; color: var(--body-ink); text-align: justify; }

  .sidebar { position: absolute; left: 800px; top: 0; width: 188px; height: 1000px; background: var(--orange); }
  .sidebar-disc { position: absolute; left: 2px; top: -8px; width: 186px; height: 186px; border-radius: 50%; background: radial-gradient(circle at 50% 40%, var(--yellow), var(--orange-deep)); }
  .sidebar-label { position: absolute; left: 0; top: 190px; width: 188px; text-align: center; font-family: "Questrial", sans-serif; font-size: 32px; line-height: 31px; color: var(--white); letter-spacing: -0.5px; }
  .sidebar-photo { position: absolute; left: 0; top: 740px; width: 188px; height: 260px; background: linear-gradient(to bottom, var(--orange) 0%, #c9b39a 10%, #8a8680 35%, #5e5a55 70%, #7c7975 100%); }
</style>
</head>
<body>
<div class="canvas">
  <main class="page">
    <header class="brand">
      <span class="brand-name">Brightwell Communications</span>
      <span class="brand-dot"></span>
    </header>

    <div class="title-band"><h1>Lorem ipsum dolor sit amet, consectetur.</h1></div>

    <section class="column column-left">
      <p>Lorem ipsum dolor sit amet, consectetur adipiscing elit. Donec mattis tincidunt tempor. Sed ullamcorper massa eget justo lacinia sit amet sagittis odio tempor. Phasellus adipiscing neque ut metus commodo eu posuere purus sollicitudin. Cras eu nibh justo. Quisque blandit placerat nisl, non vestibulum ipsum pretium vehicula. Etiam dignissim felis sed risus varius ac scelerisque massa aliquam. Aenean dignissim sagittis lacus vel porta. Pellentesque non diam leo. Donec semper dolor elementum metus cursus in tincidunt magna sagittis. Aenean sagittis tincidunt quam, non blandit elit posuere eget. Ut imperdiet urna non dolor interdum non interdum nibh lobortis. Suspendisse potenti.</p>
      <p>Etiam non scelerisque justo. Vivamus sit amet tellus massa. Cum sociis natoque penatibus et magnis dis parturient montes, nascetur ridiculus mus. Mauris dolor lorem, ornare in sagittis a, rhoncus ac urna. Sed eget sem in purus scelerisque rutrum. Aliquam erat volutpat. Duis adipiscing nulla suscipit purus condimentum non pellentesque nisi lobortis. Morbi elementum pellentesque elementum. Maecenas lobortis lacinia lacus, at elementum turpis tempor at.</p>
      <p>Sed odio ligula, faucibus a tristique et, convallis ac mi. Nulla pharetra nisl sed nisi fermentum adipiscing. Vivamus non blandit quam. Suspendisse iaculis consectetur est eget consequat. Morbi interdum, velit in auctor aliquet, tortor nisl semper elit, in iaculis urna mauris vitae massa.</p>
    </section>

    <section class="column column-right">
      <p>Lorem ipsum dolor sit amet, consectetur adipiscing elit. Donec mattis tincidunt tempor. Sed ullamcorper massa eget justo lacinia sit amet sagittis odio tempor. Phasellus adipiscing neque ut metus commodo eu posuere purus sollicitudin. Cras eu nibh justo. Quisque blandit placerat nisl, non vestibulum ipsum pretium vehicula. Etiam dignissim felis sed risus varius ac scelerisque massa aliquam. Aenean dignissim sagittis lacus vel porta. Pellentesque non diam leo. Donec semper dolor elementum metus cursus in tincidunt magna sagittis. Aenean sagittis tincidunt quam, non blandit elit posuere eget. Ut imperdiet urna non dolor interdum non interdum nibh lobortis. Suspendisse potenti.</p>
      <p>Etiam non scelerisque justo. Vivamus sit amet tellus massa. Cum sociis natoque penatibus et magnis dis parturient montes, nascetur ridiculus mus. Mauris dolor lorem, ornare in sagittis a, rhoncus ac urna. Sed eget sem in purus scelerisque rutrum. Aliquam erat volutpat. Duis adipiscing nulla suscipit purus condimentum non pellentesque nisi lobortis. Morbi elementum pellentesque elementum. Maecenas lobortis lacinia lacus, at elementum turpis tempor at.</p>
      <p>Sed odio ligula, faucibus a tristique et, convallis ac mi. Nulla pharetra nisl sed nisi fermentum adipiscing. Vivamus non blandit quam. Suspendisse iaculis consectetur est eget consequat. Morbi interdum, velit in auctor aliquet, tortor nisl semper elit, in iaculis urna mauris vitae massa.</p>
    </section>

    <footer class="summary">
      <p>Vestibulum elit urna, consectetur vitae sodales non, pretium a felis. In adipiscing, dui sed gravida luctus, neque lorem blandit ipsum, ac convallis odio nisi id dui. Aenean ac velit eget magna lobortis molestie. Praesent ullamcorper vehicula aliquet. Donec nisl sem, vulputate vitae egestas nec, egestas iaculis risus. Mauris et volutpat ligula. Vestibulum elit urna, consectetur vitae sodales non, pretium a felis. In adipiscing, dui sed gravida luctus, neque lorem blandit ipsum, ac convallis odio nisi id dui. Aenean ac velit eget magna lobortis molestie. Praesent ullamcorper vehicula aliquet. Donec nisl sem, vulputate vitae egestas nec, egestas iaculis risus. Mauris et volutpat ligula.</p>
    </footer>
  </main>

  <aside class="sidebar">
    <div class="sidebar-disc"></div>
    <div class="sidebar-label">PUBLIC<br>WORKSHOP</div>
    <div class="sidebar-photo" role="img" aria-label="Photo of participants gathered around a table with maps at a public workshop"></div>
  </aside>
</div>
</body>
</html>
```